Endocrinologist needs new stationery

I have a logo from MarkForge and now need stationery with the new logo.

Address: Suite 4, 282 Falcon Street, Richmond, VIC 3121
Phone: 03 9417 2253
Fax: 03 9417 2255
Website: www.drmaylacorwen.com.au
Email: admin@drmaylacorwen.com.au

```html
<!DOCTYPE html>
<html lang="en">
<head>
<meta charset="utf-8">
<title>Dr Mayla Corwen – Stationery</title>
<link href="https://fonts.googleapis.com/css2?family=Poppins:wght@400;500&family=PT+Sans:wght@400&display=swap" rel="stylesheet">
<style>
  :root{
    --backdrop:#8e8f92;
    --paper:#ffffff;
    --brand-blue:#336d9f;
    --ink:#2b2b2b;
    --ink-soft:#555555;
    --rule:#2f6aa0;
  }
  *{box-sizing:border-box;margin:0;padding:0}
  html,body{width:1200px;height:800px;overflow:hidden}
  body{background:var(--backdrop);position:relative;font-family:"Poppins",sans-serif;color:var(--ink)}
  .sheet{position:absolute;background:var(--paper);box-shadow:0 2px 8px rgba(0,0,0,.25)}
  .brand-name{font-family:"Poppins",sans-serif;font-weight:400;color:var(--brand-blue);white-space:nowrap;letter-spacing:.02em}

  /* Letterhead */
  .letterhead{left:143px;top:112px;width:407px;height:575px}
  .letterhead .brand-name{position:absolute;left:38px;top:40px;font-size:15px}
  .contact-block{position:absolute;border-left:1px solid var(--rule);padding-left:8px;line-height:1.3;white-space:nowrap}
  .letterhead .contact-block{left:239px;top:28px;height:63px;font-size:7.6px}
  .contact-block .address{margin-bottom:3px}
  .contact-line{display:flex;align-items:center;gap:3px}
  .contact-line svg{flex:none;fill:var(--brand-blue)}
  .recipient{position:absolute;left:39px;top:135px;font-family:"PT Sans",sans-serif}
  .recipient .name{font-size:8px;font-weight:400;text-transform:uppercase}
  .recipient .meta{font-size:5.6px;color:var(--ink-soft);line-height:1.8}
  .letter-body{position:absolute;left:39px;top:197px;width:330px;font-family:"PT Sans",sans-serif;font-weight:400;font-size:5.4px;line-height:10px;color:var(--ink);text-align:justify}
  .letter-body p{margin-bottom:8.5px}
  .closing{position:absolute;left:39px;top:427px;font-family:"PT Sans",sans-serif;font-size:6px}
  .signature-mark{position:absolute;left:44px;top:438px;width:44px;height:16px;background:linear-gradient(90deg,#e8e8e8,#f2f2f2)}
  .signer{position:absolute;left:39px;top:458px;font-family:"PT Sans",sans-serif;font-weight:400;font-size:20px;color:#444}

  /* Business cards */
  .card{top:113px;width:211px;height:120px;border-radius:9px}
  .card-front{left:614px;background:var(--brand-blue);display:flex;align-items:center;justify-content:center}
  .card-front .brand-name{color:#fff;font-size:18px}
  .card-back{left:845px}
  .card-back .brand-name{position:absolute;left:13px;top:52px;font-size:8.4px}
  .card-back .contact-block{left:104px;top:34px;height:52px;font-size:5px;padding-left:6px;line-height:1.45}
  .card-back .contact-block .address{margin-bottom:1px}

  /* Envelopes */
  .envelope-front{left:614px;top:268px;width:442px;height:191px}
  .envelope-front .brand-name{position:absolute;left:14px;top:14px;font-size:16px}
  .envelope-front .return-address{position:absolute;left:28px;top:47px;width:120px;text-align:center;font-size:7.4px;line-height:1.3;white-space:nowrap}
  .envelope-back{left:613px;top:493px;width:444px;height:194px}
  .envelope-back .flap{position:absolute;left:0;top:0}
  .envelope-back .brand-name{position:absolute;left:0;right:0;top:17px;text-align:center;color:#fff;font-size:28px}
</style>
</head>
<body>

<section class="sheet letterhead">
  <div class="brand-name">Dr Mayla Corwen</div>
  <div class="contact-block">
    <div class="address">Suite 4, 282 Falcon Street,<br>Ashmere, VIC 3189</div>
    <div class="contact-line"><svg width="6" height="6" viewBox="0 0 10 10"><path d="M2 1l2 2-1 1.5c.7 1.3 1.7 2.3 3 3L7.5 6l2 2-1.5 1.5C4.5 9 1 5.5.5 2.5z"/></svg>03 9417 2253</div>
    <div class="contact-line"><svg width="6" height="6" viewBox="0 0 10 10"><rect x="2.5" y="0.5" width="5" height="3"/><rect x="0.5" y="3.5" width="9" height="4" rx="1"/><rect x="2.5" y="7" width="5" height="2.5"/></svg>03 9417 2255</div>
    <div class="contact-line"><svg width="6" height="5" viewBox="0 0 10 8"><path d="M0 0h10v1L5 4 0 1z"/><path d="M0 2l5 3 5-3v6H0z"/></svg>admin@drmaylacorwen.com.au</div>
    <div class="contact-line"><svg width="6" height="6" viewBox="0 0 10 10"><circle cx="5" cy="5" r="4.5"/><path d="M.5 5h9M5 .5c-2 2.5-2 6.5 0 9M5 .5c2 2.5 2 6.5 0 9" stroke="#fff" stroke-width=".7" fill="none"/></svg>www.drmaylacorwen.com.au</div>
  </div>

  <div class="recipient">
    <div class="name">Halvoran</div>
    <div class="meta">Owner<br>City/State, Zip Code</div>
  </div>

  <div class="letter-body">
    <p>Lorem ipsum dolor sit amet, consectetur adipiscing elit, sed do eiusmod tempor incididunt ut labore et dolore magna aliqua. Ut enim ad minim veniam, quis nostrud exercitation ullamco laboris nisi ut aliquip ex ea commodo consequat. Duis aute irure dolor in reprehenderit in voluptate velit esse</p>
    <p>commonly used in graphic design, publishing, and web development. It is typically a corrupted version of De finibus bonorum et malorum, a 1st-century BC text by the Roman statesman and philosopher Cicero, with words altered, added, and removed to make it nonsensical and improper Latin. The first two words are the truncation of dolorem ipsum ("pain itself"). Lorem ipsum's purpose is to permit a page layout to be designed, independently of the copy that will subsequently populate it, or to demonstrate various fonts of a typeface without meaningful text that could be distracting.</p>
    <p>At vero eos et accusamus et iusto odio dignissimos ducimus, qui blanditiis praesentium voluptatum deleniti atque corrupti, quos dolores et quas molestias excepturi sint, obcaecati cupiditate non provident, similique sunt in culpa, qui officia deserunt mollitia animi, id est laborum et dolorum fuga. Et harum quidem reru[d]um facilis est e[r]t expedita distinctio. Nam libero tempore, cum soluta nobis est eligendi optio, cumque nihil impedit, quo minus id, quod maxime placeat facere possimus, omnis voluptas assumenda est, omnis dolor repellend[a]us. Temporibus autem quibusdam et aut officiis debitis aut rerum necessitatibus saepe eveniet, ut et voluptates repudiandae sint et molestiae non recusandae. Itaque earum rerum hic tenetur a sapiente delectus, ut aut reiciendis voluptatibus maiores alias consequatur aut perferendis doloribus asperiores repellat.</p>
  </div>

  <div class="closing">Sincerely,</div>
  <div class="signature-mark" role="img" aria-label="Handwritten signature"></div>
  <div class="signer">Halvoran</div>
</section>

<section class="sheet card card-front">
  <div class="brand-name">Dr Mayla Corwen</div>
</section>

<section class="sheet card card-back">
  <div class="brand-name">Dr Mayla Corwen</div>
  <div class="contact-block">
    <div class="address">Suite 4, 282 Falcon Street,<br>Ashmere, VIC 3189</div>
    <div class="contact-line"><svg width="5" height="5" viewBox="0 0 10 10"><path d="M2 1l2 2-1 1.5c.7 1.3 1.7 2.3 3 3L7.5 6l2 2-1.5 1.5C4.5 9 1 5.5.5 2.5z"/></svg>03 9417 2253</div>
    <div class="contact-line"><svg width="5" height="5" viewBox="0 0 10 10"><rect x="2.5" y="0.5" width="5" height="3"/><rect x="0.5" y="3.5" width="9" height="4" rx="1"/><rect x="2.5" y="7" width="5" height="2.5"/></svg>03 9417 2255</div>
    <div class="contact-line"><svg width="5" height="5" viewBox="0 0 10 10"><circle cx="5" cy="5" r="4.5"/><path d="M.5 5h9M5 .5c-2 2.5-2 6.5 0 9M5 .5c2 2.5 2 6.5 0 9" stroke="#fff" stroke-width=".7" fill="none"/></svg>www.drmaylacorwen.com.au</div>
    <div class="contact-line"><svg width="5" height="4" viewBox="0 0 10 8"><path d="M0 0h10v1L5 4 0 1z"/><path d="M0 2l5 3 5-3v6H0z"/></svg>admin@drmaylacorwen.com.au</div>
  </div>
</section>

<section class="sheet envelope-front">
  <div class="brand-name">Dr Mayla Corwen</div>
  <div class="return-address">Suite 4, 282 Falcon Street,<br>Ashmere, VIC 3189</div>
</section>

<section class="sheet envelope-back">
  <svg class="flap" width="444" height="72" viewBox="0 0 444 72">
    <path d="M0 0H444L432 50Q427 70 405 70H39Q17 70 12 50Z" fill="var(--brand-blue)"/>
  </svg>
  <div class="brand-name">Dr Mayla Corwen</div>
</section>

</body>
</html>
```